Business card for Mortgage broker business

I have already had the logo designed and am needing a great looking business card. My business focus is on servicing clients who may not be able to obtain finance through traditional lenders due to bad credit, short term employment or they just don't fit the banks profile. It needs to be professional, trust worthy but also have a caring fell about it.
I have provided files showing the green and black logo, the white logo(on white background so the file looks blank) and also a file with the white logo with a background of leaves that was made up which will probably be used for a website header.

Industry/Entity Type

Finance

Contact Information for Business Card

Marcus Dalby
Managing Director, Accredited Finance Broker(AFB)
Po Box 817, Pakenham VIC 3810
marcus@kestrelfunding.com.au
www.kestrelfunding.com.au
0438 216 507

Requirements
Nice to have
• I have added a picture of myself as I would like to see some designs with the pic in it, but I'm not sure if I want it on there with the logo's or just the logo's

```html
<!DOCTYPE html>
<html lang="en">
<head>
<meta charset="UTF-8">
<title>Kestrel Funding – Business Card</title>
<link rel="stylesheet" href="https://fonts.googleapis.com/css2?family=Montserrat:wght@400;500;700&display=swap">
<style>
  :root {
    --canvas: #2b2b2d;
    --card-white: #ffffff;
    --forest: #16302a;
    --brand-green: #0f7a3a;
    --ink: #1f2a26;
    --leaf-amber: #e0892a;
    --leaf-olive: #a7a53a;
    --leaf-rust: #b4471c;
    --portrait-dark: #3a2a24;
  }
  * { box-sizing: border-box; margin: 0; padding: 0; }
  html, body { width: 1200px; height: 900px; overflow: hidden; }
  body {
    background: var(--canvas);
    font-family: "Montserrat", sans-serif;
    position: relative;
  }
  .card {
    position: absolute;
    width: 640px;
    height: 391px;
    border-radius: 22px;
    overflow: hidden;
    box-shadow: 0 18px 40px rgba(0,0,0,0.45);
  }

  /* Front */
  .card-front { left: 110px; top: 50px; }
  .front-backdrop {
    position: absolute; inset: 0;
    background:
      radial-gradient(circle at 30% 60%, rgba(167,165,58,0.85) 0%, rgba(167,165,58,0) 45%),
      radial-gradient(circle at 15% 20%, rgba(180,71,28,0.8) 0%, rgba(180,71,28,0) 35%),
      linear-gradient(135deg, var(--leaf-amber) 0%, #c96a1f 55%, #5a2413 100%);
  }
  .front-portrait {
    position: absolute; right: 0; top: 0;
    width: 290px; height: 100%;
    background: linear-gradient(180deg, #6b2a18 0%, var(--portrait-dark) 45%, #1c1c22 100%);
  }
  .front-logo {
    position: absolute; left: 60px; top: 168px;
    display: flex; align-items: center; gap: 12px;
    color: var(--card-white);
    font-weight: 700; font-size: 34px; letter-spacing: 0.5px;
  }
  .logo-dot { width: 16px; height: 16px; border-radius: 50%; background: currentColor; }
  .front-web {
    position: absolute; left: 40px; bottom: 30px;
    color: var(--card-white); font-size: 17px; font-weight: 500;
  }

  /* Back */
  .card-back { left: 450px; top: 470px; background: var(--card-white); }
  .back-panel { position: absolute; inset: 0; }
  .back-accent {
    position: absolute; right: 0; top: 52px;
    width: 28px; height: 42px; background: var(--brand-green);
  }
  .back-identity {
    position: absolute; right: 42px; top: 48px; text-align: right; color: var(--ink);
  }
  .back-name { color: var(--brand-green); font-weight: 700; font-size: 27px; line-height: 1.1; }
  .back-role { font-size: 14px; line-height: 1.35; margin-top: 4px; }
  .back-logo {
    position: absolute; left: 40px; top: 140px;
    display: flex; align-items: center; gap: 10px;
    color: var(--brand-green); font-weight: 700; font-size: 30px;
  }
  .back-contact {
    position: absolute; left: 42px; bottom: 24px;
    color: var(--card-white); font-size: 15px; line-height: 1.55;
  }
  .back-contact li { list-style: none; display: flex; align-items: center; gap: 10px; }
  .back-contact svg { width: 13px; height: 13px; flex: none; }
  .back-contact strong { font-weight: 700; }
</style>
</head>
<body>

<section class="card card-front">
  <div class="front-backdrop" role="img" aria-label="Soft-focus photo of autumn maple leaves in orange, olive and rust tones"></div>
  <div class="front-portrait" role="img" aria-label="Portrait photo of the broker in a dark suit and tie"></div>
  <div class="front-logo"><span class="logo-dot"></span>Kestrel Funding</div>
  <div class="front-web">www.<strong>kestrelfunding</strong>.com.au</div>
</section>

<section class="card card-back">
  <svg class="back-panel" viewBox="0 0 640 391" preserveAspectRatio="none" aria-hidden="true">
    <path d="M0 228 L285 228 Q300 228 314 220 L400 172 Q412 165 428 165 L640 165 L640 391 L0 391 Z" fill="#16302a"/>
  </svg>
  <div class="back-accent"></div>
  <div class="back-identity">
    <div class="back-name">Marcus Dalby</div>
    <div class="back-role">Managing Director<br>Accredited Finance Broker(AFB)</div>
  </div>
  <div class="back-logo"><span class="logo-dot"></span>Kestrel Funding</div>
  <ul class="back-contact">
    <li>Po Box 817</li>
    <li>Pakenham VIC 3810</li>
    <li>
      <svg viewBox="0 0 16 16"><path fill="#fff" d="M3.6 1.5l2.3 2.6-1.3 1.8c.9 2 2.5 3.6 4.5 4.5l1.8-1.3 2.6 2.3-1.2 2.1C7 13.3 2.7 9 2 3.7z"/></svg>
      <span>0438 216 507</span>
    </li>
    <li>
      <svg viewBox="0 0 16 16"><rect x="1.5" y="3.5" width="13" height="9" fill="none" stroke="#fff" stroke-width="1.5"/><path d="M1.5 3.5L8 9l6.5-5.5" fill="none" stroke="#fff" stroke-width="1.5"/></svg>
      <span>marcus@kestrelfunding.com.au</span>
    </li>
    <li>
      <svg viewBox="0 0 16 16"><circle cx="8" cy="8" r="6.5" fill="none" stroke="#fff" stroke-width="1.5"/><path d="M1.5 8h13M8 1.5c-3 3.5-3 9.5 0 13M8 1.5c3 3.5 3 9.5 0 13" fill="none" stroke="#fff" stroke-width="1.2"/></svg>
      <span>www.<strong>kestrelfunding</strong>.com.au</span>
    </li>
  </ul>
</section>

</body>
</html>
```